Tobrin Pelmo Broth is looking for a DL Flyer for their unique food the #velmorabroth

We're looking for a punchy flyer which depicts our food dish and includes a small blurb on the front & back. Flyer size is portrait style DL (210 x 99mm) & must be 'Press Ready Files'.
Brief: Flyer background is light wooden chopping board with vertical strips.

(Text: Calibri Body or similar text, must be easy to read! Minimum 50% width)
TvR proudly present..
(Text: Calibri Body Header or similar text, must be easy to read! Min. 75% width) PELMO BROTH

Below the text PELMO BROTH insert an image (size is approx 25% of Flyer) of Borneo with a reference to Kuching. Map of Borneo can be an outline or similar but not too prominent.
Overlay the top of the map with the following text in Monotype Corsivab or similar! but must be easy to read.
Text: Kuching (2 sizes larger) Capital City of Sarawak on the Island of Borneo is home to some of the world’s greatest and unique dishes.
(new line) TvR will take you on a culinary journey to Kuching with a favourite local dish the
(new line) #VelmoraBroth (double space) so sit back, relax & enjoy!

Insert and centre the attached image DSC_0927.JPG
Remove the spoon and make the image more vibrant, do not change the colour of the soup.
Refer to attached file Flyer.jpg for images of chopsticks, a boiled egg and ingredients at the bottom. We like the lines to point to key ingredients e.g. to the egg, prawns etc. current design the font is difficult to read.

List contact details toward the bottom.
e: TvR.PelmoBroth@quillmail.example
m: +61 437152096
f : Tobrin Pelmo Broth

on the reverse of the Flyer:
Background is light wooden chopping board with vertical strips, same as front.

Refer to below link for text & Nutritional Values table.
The text for the main four paragraphs should be the key note and majority.
Note the Ingredients and the Nutritional Values table size is max 12.5% of the total Flyer size.

https://files.dorvanshare.example/doc/7QmTx83LwPzR2nVb5KcYe0HsJd4UfAi6Go1tNr9/edit

Target Market(s)

An international foody with a sense of adventure. The dish is nutritional, Gluten Free and a healthy meal. It will be sold at food markets, to office workers for lunch and for a lighter evening meal.

Industry/Entity Type

Food Production

Colors

Designer to choose colors to be used in the design.

Requirements
Must have
• 'TvR proudly present..' must be a statement along with the product 'PELMO BROTH'
• The map of Borneo with reference to Kuching, the home of the product.
• A picture of the dish itself.

```html
<!DOCTYPE html>
<html lang="en">
<head>
<meta charset="utf-8">
<title>TvR Proudly Present – Pelmo Broth DL Flyer</title>
<link href="https://fonts.googleapis.com/css2?family=Montserrat:wght@700;800&family=Raleway:wght@400;500;700&family=Cormorant+Garamond:ital,wght@1,500;1,600&display=swap" rel="stylesheet">
<style>
  :root {
    --page-bg: #ebebeb;
    --flyer-bg: #1b1b1b;
    --flyer-bg-edge: #121212;
    --orange: #f7941d;
    --white: #ffffff;
    --soft-white: #e9e9e9;
    --label-grey: #3a3a3a;
    --footer-text: #1a1a1a;
    --table-line: #8c8c8c;
    --pin-red: #d0202e;
    --map-faint: #262626;
  }
  * { box-sizing: border-box; margin: 0; padding: 0; }
  html, body {
    width: 1200px; height: 1041px; overflow: hidden;
    background: var(--page-bg);
  }
  .canvas { position: relative; width: 1200px; height: 1041px; }

  .flyer {
    position: absolute; top: 45px; width: 528px; height: 900px;
    background: radial-gradient(ellipse at 50% 40%, var(--flyer-bg) 0%, var(--flyer-bg-edge) 100%);
    overflow: hidden; color: var(--white);
  }
  .flyer > * { z-index: 2; }
  .flyer > .map-area, .flyer > .ingredients-strip { z-index: 0; }
  .flyer > .dish-photo { z-index: 1; }
  .flyer--front { left: 42px; }
  .flyer--back { left: 620px; }

  .side-label {
    position: absolute; top: 980px; width: 528px; text-align: center;
    font-family: "Raleway", sans-serif; font-size: 26px; letter-spacing: 1px;
    color: var(--label-grey);
  }
  .side-label--front { left: 42px; }
  .side-label--back { left: 620px; }

  .presenter {
    position: absolute; top: 20px;
    font-family: "Raleway", sans-serif; font-weight: 500; font-size: 18px;
    color: var(--soft-white);
  }
  .flyer--front .presenter { left: 22px; }
  .flyer--back .presenter { left: 0; width: 100%; text-align: center; }

  .product-title {
    position: absolute; font-family: "Montserrat", sans-serif; font-weight: 800;
    color: var(--orange); letter-spacing: 0.5px;
  }
  .flyer--front .product-title { left: 20px; top: 48px; font-size: 61px; line-height: 48px; }
  .flyer--back .product-title { left: 0; width: 100%; text-align: center; top: 46px; font-size: 56px; line-height: 60px; }

  .map-area { position: absolute; }
  .map-area--front { left: 338px; top: 0; width: 190px; height: 195px; }
  .map-area--back { left: 330px; top: 0; width: 198px; height: 250px; }
  .map-pin {
    position: absolute; left: 364px; top: 71px;
    font-family: "Raleway", sans-serif; font-size: 9px; color: var(--pin-red);
    display: flex; align-items: center; gap: 2px;
  }

  .script {
    font-family: "Cormorant Garamond", serif; font-style: italic; font-weight: 500;
    color: var(--soft-white);
  }
  .intro {
    position: absolute; left: 23px; top: 160px; width: 318px;
    font-size: 14px; line-height: 18.5px;
  }
  .intro strong {
    font-family: "Montserrat", sans-serif; font-style: normal; font-weight: 700;
    font-size: 18px; color: var(--white);
  }
  .journey {
    position: absolute; left: 30px; top: 224px; width: 470px; text-align: center;
    font-size: 14px; line-height: 24px;
  }
  .journey .hashtag {
    font-family: "Raleway", sans-serif; font-style: normal; font-weight: 500;
    font-size: 19px; color: var(--orange); margin-right: 4px;
  }

  .dish-photo { position: absolute; left: 22px; top: 300px; width: 506px; height: 460px; }
  .callout {
    position: absolute; font-size: 12px; line-height: 16px; text-align: center;
    color: var(--soft-white);
  }
  .callout--prawns { left: 318px; top: 303px; width: 90px; }
  .callout--chicken { left: 14px; top: 575px; width: 80px; }
  .callout--beancurd { left: 430px; top: 639px; width: 80px; }
  .callout--egg { left: 140px; top: 719px; width: 100px; }
  .callout-lines { position: absolute; left: 0; top: 0; width: 528px; height: 900px; pointer-events: none; }

  .ingredients-strip { position: absolute; left: 0; width: 528px; }
  .flyer--front .ingredients-strip { top: 680px; height: 175px; }
  .flyer--back .ingredients-strip { top: 748px; height: 107px; }

  .contact-bar {
    position: absolute; left: 0; top: 855px; width: 528px; height: 34px;
    background: var(--orange);
    display: flex; align-items: center; justify-content: space-between;
    padding: 0 16px 0 14px;
    font-family: "Raleway", sans-serif; font-weight: 700; font-size: 10.5px;
    color: var(--footer-text);
  }
  .contact-item { display: flex; align-items: center; gap: 5px; white-space: nowrap; }
  .contact-dot {
    width: 14px; height: 14px; border-radius: 50%; background: #c0281c;
    display: inline-flex; align-items: center; justify-content: center;
  }

  .story {
    position: absolute; left: 42px; top: 114px; width: 448px;
    font-size: 15px; line-height: 18.4px;
  }
  .story p { margin-bottom: 18.4px; }
  .story .highlight { color: var(--orange); }

  .ingredients-note {
    position: absolute; left: 46px; top: 478px; width: 390px;
    font-family: "Raleway", sans-serif; font-size: 11px; line-height: 15px; color: var(--soft-white);
  }
  .ingredients-note b { color: var(--orange); font-weight: 700; }

  .nutrition {
    position: absolute; left: 132px; top: 553px; width: 264px;
    border-collapse: collapse;
    font-family: "Raleway", sans-serif; font-size: 12px; color: var(--soft-white);
    background: var(--flyer-bg);
  }
  .nutrition th, .nutrition td { border: 1px solid var(--table-line); }
  .nutrition .nutrition-head {
    height: 27px; color: var(--orange); font-weight: 700; font-size: 12.5px; text-align: center;
  }
  .nutrition .nutrition-sub { height: 21px; font-weight: 400; font-size: 12.5px; text-align: center; }
  .nutrition td { height: 23.6px; padding: 0 9px; }
  .nutrition td:last-child { text-align: right; }
  .nutrition tbody tr td { border-top: none; border-bottom: none; }
  .nutrition tbody tr:last-child td { border-bottom: 1px solid var(--table-line); }
</style>
</head>
<body>
<div class="canvas">

  <!-- FRONT -->
  <section class="flyer flyer--front">
    <svg class="map-area map-area--front" role="img" aria-label="Map of Borneo with Kuching marked" viewBox="0 0 190 195">
      <defs>
        <linearGradient id="mapTone" x1="0" y1="0" x2="0" y2="1">
          <stop offset="0" stop-color="#e4e4e4"/><stop offset="1" stop-color="#cfcfcf"/>
        </linearGradient>
      </defs>
      <rect x="0" y="0" width="190" height="195" rx="26" fill="url(#mapTone)" opacity="0.9"/>
    </svg>
    <div class="map-pin">
      <svg width="10" height="13" viewBox="0 0 10 13" aria-hidden="true"><path d="M5 0a5 5 0 0 0-5 5c0 3.5 5 8 5 8s5-4.5 5-8a5 5 0 0 0-5-5z" fill="var(--pin-red)"/><circle cx="5" cy="5" r="2" fill="#fff"/></svg>
      Kuching
    </div>

    <p class="presenter">TvR Proudly Present</p>
    <h1 class="product-title">PELMO<br>BROTH</h1>

    <p class="intro script"><strong>KUCHING</strong> Capital City of Sarawak on the Island of Borneo is home to some of the world’s greatest and unique dishes.</p>
    <p class="journey script">TvR will take you on a culinary journey to Kuching with a favourite local dish the<br><span class="hashtag">#VelmoraBroth</span> so sit back, relax &amp; enjoy</p>

    <svg class="ingredients-strip" role="img" aria-label="Fresh ingredients: lemongrass, bean curd, galangal, dried chillies, mint and garlic" viewBox="0 0 528 175" preserveAspectRatio="none">
      <defs>
        <linearGradient id="herbTone" x1="0" y1="0" x2="1" y2="0">
          <stop offset="0" stop-color="#d99a2b"/><stop offset="0.25" stop-color="#7aa04a"/>
          <stop offset="0.45" stop-color="#b56a3a"/><stop offset="0.7" stop-color="#9e2a1d"/>
          <stop offset="1" stop-color="#4f9a3a"/>
        </linearGradient>
        <linearGradient id="herbFade" x1="0" y1="0" x2="0" y2="1">
          <stop offset="0" stop-color="#fff" stop-opacity="0"/><stop offset="0.5" stop-color="#fff" stop-opacity="1"/>
        </linearGradient>
        <mask id="herbMask" maskContentUnits="objectBoundingBox"><rect width="1" height="1" fill="url(#herbFade)"/></mask>
      </defs>
      <rect width="528" height="175" fill="url(#herbTone)" mask="url(#herbMask)"/>
    </svg>

    <svg class="dish-photo" role="img" aria-label="Photo of a bowl of broth with noodles, prawns, chicken, bean curd and egg, with chopsticks beside" viewBox="0 0 506 460">
      <defs>
        <radialGradient id="bowlTone" cx="0.5" cy="0.5" r="0.5">
          <stop offset="0" stop-color="#b3673e"/>
          <stop offset="0.55" stop-color="#8a4a2c"/>
          <stop offset="0.72" stop-color="#f3f1ee"/>
          <stop offset="1" stop-color="#ffffff"/>
        </radialGradient>
      </defs>
      <circle cx="260" cy="223" r="184" fill="url(#bowlTone)"/>
    </svg>

    <svg class="callout-lines" aria-hidden="true" viewBox="0 0 528 900">
      <path d="M352 330 C340 360, 335 420, 340 470" fill="none" stroke="#fff" stroke-width="0.8"/>
      <path d="M60 568 C80 530, 120 520, 180 515" fill="none" stroke="#fff" stroke-width="0.8"/>
      <path d="M470 635 C478 600, 470 580, 462 568" fill="none" stroke="#fff" stroke-width="0.8"/>
      <path d="M182 714 L182 600" fill="none" stroke="#fff" stroke-width="0.8"/>
    </svg>
    <p class="callout callout--prawns script">King Prawns</p>
    <p class="callout callout--chicken script">Chicken<br>Breast</p>
    <p class="callout callout--beancurd script">Fried Bean<br>Curd</p>
    <p class="callout callout--egg script">Free Range Egg<br>(Add-ons)</p>

    <footer class="contact-bar">
      <span class="contact-item"><span class="contact-dot"></span>TvR.PelmoBroth@quillmail.example</span>
      <span class="contact-item"><span class="contact-dot"><svg width="8" height="8" viewBox="0 0 8 8" aria-hidden="true"><path d="M1.5 0.5l1.3 1.6-0.8 1c0.5 1 1.1 1.6 2 2l1-0.8 1.6 1.3-0.9 1.5C3.5 7 1 4.5 0.6 1.4z" fill="#fff"/></svg></span>+61 437152096</span>
      <span class="contact-item"><span class="contact-dot"></span>Tobrin Pelmo Broth</span>
    </footer>
  </section>

  <!-- BACK -->
  <section class="flyer flyer--back">
    <svg class="map-area map-area--back" role="img" aria-label="Faint map of Borneo" viewBox="0 0 198 250">
      <rect x="0" y="0" width="198" height="250" rx="40" fill="var(--map-faint)"/>
    </svg>
    <p class="presenter">TvR Proudly Present</p>
    <h1 class="product-title">PELMO BROTH</h1>

    <div class="story script">
      <p>Eats Malaysia: a short while ago on my travels around East Malaysia I was introduced to a place called Kuching, Capital City of Sarawak.</p>
      <p>I was overwhelmed by their number of unique dishes, from the Sea to the Borneo Jungle local sustainable ingredients are sourced to create some of Kuching’s indigenous foods.</p>
      <p>I was astonished to learn that famous Kuching dishes like Kolo Mee and the Velmora Broth are breakfast dishes and often sold out by 10am.</p>
      <p>I have chosen the Velmora Broth to share with You..<br>It converts perfectly to our requirements - a healthy, Gluten-Free nourishing meal, although maybe not breakfast for everyone!</p>
      <p><span class="highlight">The Broth sambal / base stock is made from ALL plant-based ingredients.</span><br>We add a dash of coconut milk to bring balance to this simple yet complex dish; with it’s more subtle and fine blend of aromatic herbs and spices and a hint of sour and chilli undertones.</p>
    </div>

    <p class="ingredients-note"><b>Ingredients:</b> rice vermicelli - bihoon, omelette strips (free range eggs), sliced chicken breast, King prawns, bean-sprouts, fried bean curd and garnished with lime wedge, fresh coriander and sambal on the side.</p>

    <svg class="ingredients-strip" role="img" aria-label="Fresh ingredients: lemongrass, bean curd, galangal, dried chillies, mint and garlic" viewBox="0 0 528 107" preserveAspectRatio="none">
      <rect width="528" height="107" fill="url(#herbTone)" mask="url(#herbMask)"/>
    </svg>

    <table class="nutrition">
      <thead>
        <tr><th class="nutrition-head" colspan="2">NUTRITION INFORMATION:</th></tr>
        <tr><th class="nutrition-sub" colspan="2">Pelmo Broth Per serve</th></tr>
      </thead>
      <tbody>
        <tr><td>ENERGY</td><td>1920kJ</td></tr>
        <tr><td>CALORIES</td><td>458</td></tr>
        <tr><td>PROTEIN</td><td>30g</td></tr>
        <tr><td>GLUTEN</td><td>UNDETECTED</td></tr>
        <tr><td>FAT - TOTAL</td><td>38g</td></tr>
        <tr><td>CARBOHYDRATES</td><td>52g</td></tr>
      </tbody>
    </table>

    <footer class="contact-bar">
      <span class="contact-item"><span class="contact-dot"></span>TvR.PelmoBroth@quillmail.example</span>
      <span class="contact-item"><span class="contact-dot"><svg width="8" height="8" viewBox="0 0 8 8" aria-hidden="true"><path d="M1.5 0.5l1.3 1.6-0.8 1c0.5 1 1.1 1.6 2 2l1-0.8 1.6 1.3-0.9 1.5C3.5 7 1 4.5 0.6 1.4z" fill="#fff"/></svg></span>+61 437152096</span>
      <span class="contact-item"><span class="contact-dot"></span>Tobrin Pelmo Broth</span>
    </footer>
  </section>

  <p class="side-label side-label--front">FRONT</p>
  <p class="side-label side-label--back">BACK</p>
</div>
</body>
</html>
```